Simple and clean

We need a business card design for a new company called Dwelling Owl. It is a search engine to find current properties for sale or rent in New Zealand market.
We have already a colour scheme that we would like people to use.
Light brown: #D4CCB0
Light green: #D6E4D4
Green: #669966
Black/White
It is OK to divert from this colour scheme slightly as long as there is a green component to the business card.
Final design should be clean, simple and should communicate the nature of the business.
Target Market(s)
- First home buyers
- Real estate agents
- People seeking rentals
Industry/Entity Type
Business
Requirements
Must have
- Use those or similar colours.
Light brown: #D4CCB0
Light green: #D6E4D4
Green: #669966
Black/White

```html
<!DOCTYPE html>
<html lang="en">
<head>
<meta charset="utf-8">
<title>Dwelling Owl – Business Card</title>
<link rel="stylesheet" href="https://fonts.googleapis.com/css2?family=Open+Sans:wght@600;700&family=Arimo:wght@400&display=swap">
<style>
  :root {
    --page-bg: #ffffff;
    --card-black: #000000;
    --card-divider: #ffffff;
    --card-lime: #94ec3e;
    --brand-light-green: #d6e4d4;
    --text-dark: #111111;
  }
  html, body {
    margin: 0;
    padding: 0;
    width: 1200px;
    height: 900px;
    overflow: hidden;
    background: var(--page-bg);
  }
  .canvas {
    width: 1200px;
    height: 900px;
    display: flex;
    align-items: center;
    justify-content: center;
  }
  .business-card {
    width: 720px;
    height: 440px;
    display: flex;
    flex-direction: column;
    background: var(--card-lime);
  }
  .card-header {
    height: 235px;
    background: var(--card-black);
    display: flex;
    align-items: center;
    padding-left: 64px;
    border-bottom: 10px solid var(--card-divider);
    box-sizing: content-box;
  }
  .brand {
    display: flex;
    align-items: center;
    gap: 18px;
    color: var(--brand-light-green);
    font-family: "Open Sans", sans-serif;
    font-weight: 600;
    font-size: 74px;
    letter-spacing: -1px;
    line-height: 1;
  }
  .brand-dot {
    width: 46px;
    height: 46px;
    border-radius: 50%;
    background: var(--brand-light-green);
    flex: none;
  }
  .card-details {
    flex: 1;
    padding: 26px 0 0 68px;
    color: var(--text-dark);
  }
  .person-name {
    margin: 0;
    font-family: "Open Sans", sans-serif;
    font-weight: 700;
    font-size: 25px;
    line-height: 1.05;
  }
  .person-role {
    margin: 0 0 14px;
    font-family: "Open Sans", sans-serif;
    font-weight: 700;
    font-size: 19px;
    line-height: 1.1;
  }
  .contact-list {
    margin: 0;
    padding: 0;
    list-style: none;
    font-family: "Arimo", Arial, sans-serif;
    font-size: 18px;
    line-height: 1.1;
  }
  .contact-web {
    margin: 14px 0 0;
    font-family: "Arimo", Arial, sans-serif;
    font-size: 18px;
  }
</style>
</head>
<body>
  <main class="canvas">
    <article class="business-card">
      <header class="card-header">
        <div class="brand">
          <span class="brand-dot" aria-hidden="true"></span>
          <span class="brand-name">Dwelling Owl</span>
        </div>
      </header>
      <section class="card-details">
        <h1 class="person-name">Sam Carter</h1>
        <p class="person-role">Director</p>
        <ul class="contact-list">
          <li>Mobile number</li>
          <li>Email address</li>
        </ul>
        <p class="contact-web">www.dwellingowl.co.nz</p>
      </section>
    </article>
  </main>
</body>
</html>
```